Fresh, modern, fun business card for pediatric dental practice

Need a business card for fresh, modern, fun pediatric dental practice

Clean look that matches our website's font and colors

We prefer the look of curved corners on business cards

Target Market(s)

parents (mothers) of young children, professionals, mid-high class

Industry/Entity Type

Dental

Contact Information for Business Card

Maplebrook Pediatric Dentistry
482 Orchard Vale Road
Suite 517
Alderwick, PA 17890
555.419.3067
www.maplebrookkidsdental.example

Mara Tevlin, DMD
Colette Varnum, DMD
(we are working on our email address, but we would like that on the card as well)

Font styles to use
Sans Serif

Requirements
Must have
• All info; we would also like to make cards for individual staff members
• colors from our website and color palatte, attatched
• use same font and design as website for branding
Nice to have
• clean, simple card that has a pop of color
• we would like to see a few designs with our tag line "where smiles get brighter"
• we are not sure if we want to have it on there or not
• we would like to see a few designs incorporating the ribbon graphic on our website where the word WELCOME is

```html
<!DOCTYPE html>
<html lang="en">
<head>
<meta charset="utf-8">
<title>Maplebrook Pediatric Dentistry – Business Card</title>
<link rel="stylesheet" href="https://fonts.googleapis.com/css2?family=Open+Sans:wght@400;600;700&family=Questrial&display=swap">
<style>
  :root {
    --sun-yellow: #f8b825;
    --berry: #d4268f;
    --plum: #51294d;
    --ink: #333333;
    --paper: #ffffff;
  }
  * { margin: 0; padding: 0; box-sizing: border-box; }
  html, body { width: 1200px; height: 800px; overflow: hidden; background: var(--paper); }
  .canvas { position: relative; width: 1200px; height: 800px; }
  .card {
    position: absolute;
    width: 498px;
    height: 284px;
    border-radius: 6px;
    overflow: hidden;
    box-shadow: 0 8px 16px rgba(0,0,0,0.22);
  }
  .card-front { left: 93px; top: 258px; background: var(--paper); }
  .card-back { left: 617px; top: 260px; background: var(--plum); }

  .wordmark {
    font-family: "Open Sans", sans-serif;
    font-weight: 600;
    color: var(--sun-yellow);
    line-height: 1;
  }
  .card-front .wordmark { position: absolute; left: 13px; top: 24px; }
  .wordmark-main { display: block; font-size: 37px; letter-spacing: 1px; }
  .wordmark-sub { display: block; font-size: 17px; letter-spacing: 2px; margin-top: 4px; }

  .dentist-name {
    position: absolute; left: 14px; top: 97px;
    font-family: "Open Sans", sans-serif; font-weight: 600;
    font-size: 19px; color: var(--berry);
  }
  .contact-list { position: absolute; left: 14px; top: 133px; list-style: none; }
  .contact-list li {
    display: flex; align-items: center; height: 19px;
    font-family: "Questrial", sans-serif; font-size: 13.5px; color: var(--ink);
  }
  .contact-list svg { width: 13px; height: 13px; margin-right: 9px; flex: none; }

  .practice-heading {
    position: absolute; left: 14px; top: 202px;
    font-family: "Open Sans", sans-serif; font-weight: 700;
    font-size: 11.5px; letter-spacing: 1px; color: var(--berry);
  }
  .practice-address {
    position: absolute; left: 14px; top: 220px;
    font-family: "Questrial", sans-serif; font-size: 12px; line-height: 15px; color: var(--ink);
    font-style: normal;
  }

  .sun-accent { position: absolute; top: 0; }
  .card-front .sun-accent { right: 0; }
  .card-back .sun-accent { left: 0; }

  .card-back .brand-lockup {
    position: absolute; left: 170px; top: 110px;
    display: flex; align-items: center;
  }
  .brand-dot {
    width: 32px; height: 32px; border-radius: 50%;
    border: 3px solid var(--sun-yellow); margin-right: 14px; flex: none;
  }
  .card-back .wordmark-main { font-size: 30px; }
  .card-back .wordmark-sub { font-size: 14px; letter-spacing: 1.6px; margin-top: 3px; }

  .back-web {
    position: absolute; right: 60px; top: 250px;
    font-family: "Questrial", sans-serif; font-size: 12.5px; color: var(--sun-yellow);
  }
  .back-web strong { font-family: "Open Sans", sans-serif; font-weight: 700; font-size: 12px; }
</style>
</head>
<body>
<main class="canvas">

  <section class="card card-front" aria-label="Business card front">
    <div class="wordmark">
      <span class="wordmark-main">maplebrook</span>
      <span class="wordmark-sub">pediatric dentistry</span>
    </div>

    <h1 class="dentist-name">Mara Tevlin, DMD</h1>

    <ul class="contact-list">
      <li>
        <svg viewBox="0 0 14 14" aria-hidden="true"><circle cx="7" cy="7" r="6.2" fill="none" stroke="var(--sun-yellow)" stroke-width="1.2"/><path d="M5 4.2l1 1.6-.7.7c.4.9 1.1 1.6 2 2l.7-.7 1.6 1-.6 1.1c-2.2-.3-4.1-2.2-4.4-4.4z" fill="var(--berry)"/></svg>
        555.419.3067
      </li>
      <li>
        <svg viewBox="0 0 14 14" aria-hidden="true"><circle cx="7" cy="7" r="6.2" fill="none" stroke="var(--sun-yellow)" stroke-width="1.2"/><rect x="4" y="5" width="6" height="4.2" fill="none" stroke="var(--berry)" stroke-width="0.9"/><path d="M4 5l3 2.3L10 5" fill="none" stroke="var(--berry)" stroke-width="0.9"/></svg>
        info@maplebrookkidsdental.example
      </li>
      <li>
        <svg viewBox="0 0 14 14" aria-hidden="true"><circle cx="7" cy="7" r="6.2" fill="none" stroke="var(--sun-yellow)" stroke-width="1.2"/><circle cx="7" cy="7" r="3" fill="none" stroke="var(--berry)" stroke-width="0.9"/><path d="M4 7h6M7 4c-1.3 1.7-1.3 4.3 0 6M7 4c1.3 1.7 1.3 4.3 0 6" fill="none" stroke="var(--berry)" stroke-width="0.7"/></svg>
        www.maplebrookkidsdental.example
      </li>
    </ul>

    <h2 class="practice-heading">MAPLEBROOK PEDIATRIC DENTISTRY</h2>
    <address class="practice-address">
      Maplebrook Pediatric Dentistry<br>
      482 Orchard Vale Road<br>
      Suite 517, Alderwick, PA 17890
    </address>

    <svg class="sun-accent" width="120" height="284" viewBox="0 0 120 284" aria-hidden="true">
      <circle cx="120" cy="142" r="78" fill="none" stroke="var(--sun-yellow)" stroke-width="8"/>
    </svg>
  </section>

  <section class="card card-back" aria-label="Business card back">
    <svg class="sun-accent" width="120" height="284" viewBox="0 0 120 284" aria-hidden="true">
      <circle cx="0" cy="156" r="78" fill="none" stroke="var(--sun-yellow)" stroke-width="8"/>
    </svg>

    <div class="brand-lockup">
      <span class="brand-dot" aria-hidden="true"></span>
      <div class="wordmark">
        <span class="wordmark-main">maplebrook</span>
        <span class="wordmark-sub">pediatric dentistry</span>
      </div>
    </div>

    <p class="back-web">www.<strong>maplebrookkidsdental</strong>.example</p>
  </section>

</main>
</body>
</html>
```